依頼詳細
封筒デザインを依頼します。封筒は相続人様にももちろん、各業者様に送る際にも使えるような万能型でお願いしたいと思います。

サイズの種類は①角2 窓なし、②長3 縦 窓なし、③長3 横 窓付きの3点で同じテイストで結構です。デザインは表面のみ、色はフルカラー、封筒の色は白を予定しています。

作成して頂いたデザインで最終的にモビタンにて発注予定のため、最終的にコンペにて選ばれた方には、下記のテンプレートの要領に従って入稿データの作成についてお願い致します。郵便番号枠は「なし」です。
https://mobitan-print.example/guide/how-to-make-data/envelope/

ロゴデータ、名刺データを添付いたします。
記載項目
表面:
・ロゴ
・事務所名
・郵便番号
・住所(建物・部屋番号まで)
・電話 (携帯電話番号不要)
FAXは利用していません。
希望イメージ
シンプル 複雑
単色 カラフル
暗い 明るい
日常 高級
遊び心 厳粛
未来的 伝統的
女性的 男性的
希望する色
青系、水色系

ご提案の文章にあるように「落ち着きのある中に気持ち先進感」なデザインが気に入りました。名刺デザインからさらに工夫を加えられており、イメージしてた以上に良いデザインをご提案いただきました。

みなさま、それぞれに素敵なデザインをご提案いただきましてありがとうございました。

```html
<!DOCTYPE html>
<html lang="ja">
<head>
<meta charset="utf-8">
<title>青葉相続専門税理士事務所 封筒デザイン</title>
<link href="https://fonts.googleapis.com/css2?family=Noto+Sans+JP:wght@400;500&display=swap" rel="stylesheet">
<style>
  :root{
    --bg:#e4e6ea;
    --paper:#ffffff;
    --ink:#1c2f5e;
    --muted:#4a5674;
    --navy:#0f2a78;
    --blue:#1f56c8;
    --sky:#8fb6ee;
    --faint:#eef2f9;
    --window:#e9eaec;
  }
  *{box-sizing:border-box;margin:0;padding:0}
  html,body{width:1200px;height:1023px;overflow:hidden}
  body{background:var(--bg);font-family:"Noto Sans JP",sans-serif;position:relative;color:var(--ink)}
  .envelope{position:absolute;background:var(--paper);overflow:hidden;border:1px solid #d5d8de}
  .envelope--kaku2{left:139px;top:165px;width:408px;height:730px}
  .envelope--naga3-vertical{left:742px;top:101px;width:256px;height:518px}
  .envelope--naga3-horizontal{left:632px;top:640px;width:404px;height:300px}

  .faint-circle{position:absolute;border-radius:50%;background:radial-gradient(circle at 40% 40%,var(--paper) 30%,var(--faint) 100%);border:2px solid #e3e9f4}

  .brand{position:absolute;display:flex;align-items:center;gap:8px}
  .brand__dot{border-radius:50%;background:var(--blue);flex:none}
  .brand__name{font-weight:500;color:var(--ink);white-space:nowrap}
  .address{position:absolute;color:var(--muted);white-space:nowrap}

  .band{position:absolute;left:0;right:0;background:linear-gradient(90deg,var(--navy) 0%,var(--blue) 45%,var(--sky) 80%,var(--blue) 100%)}
  .band::before{content:"";position:absolute;left:0;right:0;top:-5px;height:1px;background:linear-gradient(90deg,var(--navy),var(--sky))}
  .band::after{content:"";position:absolute;left:0;right:0;top:40%;height:1px;background:rgba(255,255,255,.55)}

  .window{position:absolute;left:13%;top:11%;width:45%;height:28%;background:var(--window);border-radius:4px;border:1px solid #dcdde0}
</style>
</head>
<body>

<!-- 角2 窓なし -->
<section class="envelope envelope--kaku2" aria-label="角2封筒 表面">
  <div class="faint-circle" style="left:40px;top:360px;width:260px;height:260px"></div>
  <div class="brand" style="left:120px;top:740px;top:740px">
  </div>
  <div class="brand" style="left:115px;top:630px">
    <span class="brand__dot" style="width:22px;height:22px"></span>
    <span class="brand__name" style="font-size:13px">青葉相続専門税理士事務所</span>
  </div>
  <div class="band" style="top:668px;height:22px"></div>
  <p class="address" style="left:20px;top:698px;font-size:7px">〒150-0001 東京都渋谷区青葉町1-2-3 青葉ビル5F　TEL 03-0000-0000</p>
</section>

<!-- 長3 縦 窓なし -->
<section class="envelope envelope--naga3-vertical" aria-label="長3封筒 縦 表面">
  <div class="faint-circle" style="left:30px;top:260px;width:170px;height:170px"></div>
  <div class="brand" style="left:58px;top:415px">
    <span class="brand__dot" style="width:16px;height:16px"></span>
    <span class="brand__name" style="font-size:9px">青葉相続専門税理士事務所</span>
  </div>
  <p class="address" style="left:74px;top:440px;font-size:5px">〒150-0001 東京都渋谷区青葉町1-2-3 青葉ビル5F</p>
  <p class="address" style="left:74px;top:448px;font-size:5px">TEL 03-0000-0000</p>
  <div class="band" style="top:466px;height:18px"></div>
</section>

<!-- 長3 横 窓付き -->
<section class="envelope envelope--naga3-horizontal" aria-label="長3封筒 横 窓付き 表面">
  <div class="window"></div>
  <div class="faint-circle" style="left:300px;top:70px;width:140px;height:140px"></div>
  <div class="brand" style="left:262px;top:202px">
    <span class="brand__dot" style="width:16px;height:16px"></span>
    <span class="brand__name" style="font-size:9px">青葉相続専門税理士事務所</span>
  </div>
  <p class="address" style="left:262px;top:226px;font-size:5px">〒150-0001 東京都渋谷区青葉町1-2-3 青葉ビル5F</p>
  <p class="address" style="left:262px;top:234px;font-size:5px">TEL 03-0000-0000</p>
  <div class="band" style="top:256px;height:20px"></div>
</section>

</body>
</html>
```